Looking for a creative label design for our retail coffee bags

We are a coffee manufacturer (coffee roaster) looking to re-brand our retail label for our coffee bags. Our main coffee blend that we sell is our Harborline Velvet Blend. You can use this name when creating the label. We are going for a look that represents our company as a coffee roaster. Please reference our website (www.brindlemugworks.com) and our Facebook page to learn more about our company and to give you more inspiration on creating this design.

Target Market(s)

Retail customers/grocery stores

Industry/Entity Type

Manufacturer

Requirements
Must have
• The size of the label has to be 3" width x 4" height

Logo must be Black
Nice to have
• We currently incorporate a color on our labels for each blend. For example, Harborline Velvet Blend (royal blue), Decaffeinated Blend (red), Breakfast Blend (green), Flavored coffees (gold).

Rustic/vintage style

```html
<!DOCTYPE html>
<html lang="en">
<head>
<meta charset="utf-8">
<title>Brindle Mugworks – Coffee Labels</title>
<link rel="stylesheet" href="https://fonts.googleapis.com/css2?family=Sancreek&family=Rye&family=IM+Fell+DW+Pica&family=Cormorant+Garamond:wght@500&display=swap">
<style>
  :root {
    --page: #ffffff;
    --label-ink: #121212;
    --label-ink-light: #262626;
    --chalk: #f4f4f2;
    --chalk-soft: rgba(244, 244, 242, 0.22);
    --blend-blue: #4169e1;
    --blend-red: #ff1a1a;
    --blend-green: #8cc21f;
    --blend-gold: #e0b448;
    --seal: #141414;
  }
  * { box-sizing: border-box; margin: 0; padding: 0; }
  html, body { width: 1200px; height: 1200px; overflow: hidden; background: var(--page); }
  .canvas { position: relative; width: 1200px; height: 1200px; }

  .label {
    position: absolute;
    width: 516px; height: 688px;
    background: radial-gradient(ellipse at 45% 40%, var(--label-ink-light), var(--label-ink) 75%);
    color: var(--chalk);
    font-family: "IM Fell DW Pica", Georgia, serif;
  }
  .label--hero { left: 342px; top: 20px; }
  .label-slot { position: absolute; top: 835px; width: 173px; height: 230px; }
  .label-slot .label { left: 0; top: 0; transform: scale(0.3353); transform-origin: 0 0; }
  .slot-1 { left: 169px; } .slot-2 { left: 407px; } .slot-3 { left: 641px; } .slot-4 { left: 879px; }

  .frame-outer { position: absolute; inset: 10px; border: 2px solid var(--chalk); border-radius: 6px; }
  .frame-inner { position: absolute; inset: 16px; border: 1px solid var(--chalk); border-radius: 4px; }

  .corner-ornament {
    position: absolute; width: 56px; height: 56px;
    background: radial-gradient(circle, var(--chalk-soft), transparent 70%);
  }
  .corner-ornament.tl { left: 18px; top: 18px; } .corner-ornament.tr { right: 18px; top: 18px; }
  .corner-ornament.bl { left: 18px; bottom: 18px; } .corner-ornament.br { right: 18px; bottom: 18px; }

  .blend-tab { position: absolute; left: 94px; top: 0; width: 117px; height: 99px; }
  .blend-tab--blue { background: var(--blend-blue); }
  .blend-tab--red { background: var(--blend-red); }
  .blend-tab--green { background: var(--blend-green); }
  .blend-tab--gold { background: var(--blend-gold); }

  .brand-seal {
    position: absolute; left: 108px; top: 26px; width: 90px; height: 90px;
    border-radius: 50%; background: var(--seal);
    display: flex; align-items: center; justify-content: center; text-align: center;
    font-family: "IM Fell DW Pica", Georgia, serif; font-size: 15px; line-height: 1.05; color: var(--chalk);
  }

  .crest-ornament {
    position: absolute; left: 39px; top: 104px; width: 435px; height: 136px;
    background: radial-gradient(ellipse at 50% 65%, rgba(244,244,242,0.3), transparent 70%);
  }
  .divider-ornament {
    position: absolute; left: 36px; top: 440px; width: 444px; height: 66px;
    background: radial-gradient(ellipse at 50% 45%, rgba(244,244,242,0.28), transparent 72%);
  }

  .blend-name {
    position: absolute; left: 30px; right: 30px; top: 250px; height: 185px;
    text-align: center; font-weight: normal;
    display: flex; flex-direction: column; justify-content: center; align-items: center;
  }
  .blend-name span { display: block; white-space: nowrap; }
  .blend-name--western { font-family: "Sancreek", "Rye", serif; line-height: 1.05; }
  .blend-name--western .line-1 { font-size: 78px; letter-spacing: 1px; }
  .blend-name--western .line-2 { font-size: 62px; letter-spacing: 1px; }
  .blend-name--classic { font-family: "Cormorant Garamond", Georgia, serif; font-weight: 500; font-size: 62px; line-height: 1.2; letter-spacing: 2px; }
  .blend-name--flavored { font-size: 74px; }
  .blend-name--saloon { font-family: "Rye", serif; font-size: 54px; line-height: 1.3; letter-spacing: 2px; }

  .blend-story { position: absolute; left: 39px; right: 39px; top: 524px; font-size: 13.4px; line-height: 1.13; text-align: justify; letter-spacing: 0.3px; }
  .net-weight { position: absolute; left: 0; right: 0; top: 604px; text-align: center; font-size: 23px; }
  .weight-rule { position: absolute; left: 185px; width: 146px; top: 632px; height: 8px; }
</style>
</head>
<body>
<main class="canvas">

  <article class="label label--hero">
    <div class="frame-outer"></div><div class="frame-inner"></div>
    <div class="corner-ornament tl" role="img" aria-label="Victorian corner flourish"></div>
    <div class="corner-ornament tr" role="img" aria-label="Victorian corner flourish"></div>
    <div class="corner-ornament bl" role="img" aria-label="Victorian corner flourish"></div>
    <div class="corner-ornament br" role="img" aria-label="Victorian corner flourish"></div>
    <div class="blend-tab blend-tab--blue"></div>
    <div class="brand-seal">Brindle<br>Mugworks</div>
    <div class="crest-ornament" role="img" aria-label="Ornate scrollwork crest"></div>
    <h1 class="blend-name blend-name--western"><span class="line-1">Harborline</span><span class="line-2">Velvet Blend</span></h1>
    <div class="divider-ornament" role="img" aria-label="Scrolled divider flourish"></div>
    <p class="blend-story">Our Harborline Velvet Blend is our finest blend made from the best Arabica beans South America has to offer, carefully roasted to perfection. A blend for coffee connoisseurs, it's a pinnacle of our 20 years of experience in bean selection, roasting, grinding and packaging. Its distinctive rich aroma with a smooth Colombian undertone leaves people coming back for more.</p>
    <p class="net-weight">200g</p>
    <svg class="weight-rule" viewBox="0 0 146 8"><line x1="0" y1="4" x2="146" y2="4" stroke="#f4f4f2" stroke-width="1"/><circle cx="73" cy="4" r="3" fill="none" stroke="#f4f4f2"/></svg>
  </article>

  <div class="label-slot slot-1">
    <article class="label">
      <div class="frame-outer"></div><div class="frame-inner"></div>
      <div class="corner-ornament tl" role="img" aria-label="Victorian corner flourish"></div>
      <div class="corner-ornament tr" role="img" aria-label="Victorian corner flourish"></div>
      <div class="corner-ornament bl" role="img" aria-label="Victorian corner flourish"></div>
      <div class="corner-ornament br" role="img" aria-label="Victorian corner flourish"></div>
      <div class="blend-tab blend-tab--blue"></div>
      <div class="brand-seal">Brindle<br>Mugworks</div>
      <div class="crest-ornament" role="img" aria-label="Ornate scrollwork crest"></div>
      <h2 class="blend-name blend-name--western"><span class="line-1">Harborline</span><span class="line-2">Velvet Blend</span></h2>
      <div class="divider-ornament" role="img" aria-label="Scrolled divider flourish"></div>
      <p class="blend-story">A careful roast of fine Arabica beans, packed fresh for a rich aroma and a smooth, lasting finish in every cup.</p>
      <p class="net-weight">200g</p>
      <svg class="weight-rule" viewBox="0 0 146 8"><line x1="0" y1="4" x2="146" y2="4" stroke="#f4f4f2"/><circle cx="73" cy="4" r="3" fill="none" stroke="#f4f4f2"/></svg>
    </article>
  </div>

  <div class="label-slot slot-2">
    <article class="label">
      <div class="frame-outer"></div><div class="frame-inner"></div>
      <div class="corner-ornament tl" role="img" aria-label="Victorian corner flourish"></div>
      <div class="corner-ornament tr" role="img" aria-label="Victorian corner flourish"></div>
      <div class="corner-ornament bl" role="img" aria-label="Victorian corner flourish"></div>
      <div class="corner-ornament br" role="img" aria-label="Victorian corner flourish"></div>
      <div class="blend-tab blend-tab--red"></div>
      <div class="brand-seal">Brindle<br>Mugworks</div>
      <div class="crest-ornament" role="img" aria-label="Ornate scrollwork crest"></div>
      <h2 class="blend-name blend-name--classic"><span>Decaffeinated</span><span>Blend</span></h2>
      <div class="divider-ornament" role="img" aria-label="Scrolled divider flourish"></div>
      <p class="blend-story">A careful roast of fine Arabica beans, packed fresh for a rich aroma and a smooth, lasting finish in every cup.</p>
      <p class="net-weight">200g</p>
      <svg class="weight-rule" viewBox="0 0 146 8"><line x1="0" y1="4" x2="146" y2="4" stroke="#f4f4f2"/><circle cx="73" cy="4" r="3" fill="none" stroke="#f4f4f2"/></svg>
    </article>
  </div>

  <div class="label-slot slot-3">
    <article class="label">
      <div class="frame-outer"></div><div class="frame-inner"></div>
      <div class="corner-ornament tl" role="img" aria-label="Victorian corner flourish"></div>
      <div class="corner-ornament tr" role="img" aria-label="Victorian corner flourish"></div>
      <div class="corner-ornament bl" role="img" aria-label="Victorian corner flourish"></div>
      <div class="corner-ornament br" role="img" aria-label="Victorian corner flourish"></div>
      <div class="blend-tab blend-tab--green"></div>
      <div class="brand-seal">Brindle<br>Mugworks</div>
      <div class="crest-ornament" role="img" aria-label="Ornate scrollwork crest"></div>
      <h2 class="blend-name blend-name--saloon"><span>BREAKFAST</span><span>BLEND</span></h2>
      <div class="divider-ornament" role="img" aria-label="Scrolled divider flourish"></div>
      <p class="blend-story">A careful roast of fine Arabica beans, packed fresh for a rich aroma and a smooth, lasting finish in every cup.</p>
      <p class="net-weight">200g</p>
      <svg class="weight-rule" viewBox="0 0 146 8"><line x1="0" y1="4" x2="146" y2="4" stroke="#f4f4f2"/><circle cx="73" cy="4" r="3" fill="none" stroke="#f4f4f2"/></svg>
    </article>
  </div>

  <div class="label-slot slot-4">
    <article class="label">
      <div class="frame-outer"></div><div class="frame-inner"></div>
      <div class="corner-ornament tl" role="img" aria-label="Victorian corner flourish"></div>
      <div class="corner-ornament tr" role="img" aria-label="Victorian corner flourish"></div>
      <div class="corner-ornament bl" role="img" aria-label="Victorian corner flourish"></div>
      <div class="corner-ornament br" role="img" aria-label="Victorian corner flourish"></div>
      <div class="blend-tab blend-tab--gold"></div>
      <div class="brand-seal">Brindle<br>Mugworks</div>
      <div class="crest-ornament" role="img" aria-label="Ornate scrollwork crest"></div>
      <h2 class="blend-name blend-name--classic blend-name--flavored"><span>Flavored</span><span>Coffee</span></h2>
      <div class="divider-ornament" role="img" aria-label="Scrolled divider flourish"></div>
      <p class="blend-story">A careful roast of fine Arabica beans, packed fresh for a rich aroma and a smooth, lasting finish in every cup.</p>
      <p class="net-weight">200g</p>
      <svg class="weight-rule" viewBox="0 0 146 8"><line x1="0" y1="4" x2="146" y2="4" stroke="#f4f4f2"/><circle cx="73" cy="4" r="3" fill="none" stroke="#f4f4f2"/></svg>
    </article>
  </div>

</main>
</body>
</html>
```